Web-Design for Global Telecommunications Operator

We need a Wordpress web-site for our organisation "Vexlink" which is a B2B telecommunications operator with presence in Australia, Fiji, Papua New Guinea, UK, Singapore, Anguilla.

The company has multiple sides to it:
1) Carrier Wholesale - we provide international call termination to carriers globally of the likes of Marquon, KR, OP&L, Quenvo, Ramex, Soren Velacom.

2) Call Center Termination - we provide our network to call centers to be able to terminate their calls to the end user in order to perform telemarketing activities.

3) Satellite - we provide internet bandwidth via Satellite to customers from around the world

4) Consultancy - with over 35 years of experience under our belt, we believe we are fit to offer consultancy to people facing challenges within the IT&T industry.

5) B2C - Our operations globally also own various retail operations that market B2C services.

Our colours are red, white and black and we would like to stick to this theme.

Industry/Entity Type

Telecommunications

```html
<!DOCTYPE html>
<html lang="en">
<head>
<meta charset="utf-8">
<title>Vexlink — Global Telecommunications</title>
<link href="https://fonts.googleapis.com/css2?family=Roboto:wght@300;400&family=Roboto+Condensed:wght@300&family=Ubuntu:wght@400;500&family=Open+Sans:wght@400;600;700&display=swap" rel="stylesheet">
<style>
:root{
  --red:#d8141c;
  --red-deep:#c0090f;
  --red-bright:#ee1c24;
  --ink:#333333;
  --nav:#3a3a3a;
  --page-bg:#efefef;
  --white:#ffffff;
  --grey-text:#777777;
  --card-bg:#f7f7f7;
  --line:#dddddd;
  --blue:#1b5e9e;
  --footer:#3c3c3d;
  --footer-deep:#333334;
  --footer-text:#d6d6d6;
  --tweet-bar:#5b5b5c;
}
*{margin:0;padding:0;box-sizing:border-box}
html,body{width:888px;height:1200px;overflow:hidden}
body{background:var(--page-bg);font-family:"Open Sans",sans-serif;color:var(--ink);position:relative}
.site{position:absolute;left:37px;top:35px;width:816px;height:1165px;background:var(--white);border:1px solid #dcdcdc;border-bottom:0}
.abs{position:absolute}

/* header */
.brand{left:67px;top:82px;display:flex;align-items:center;gap:10px}
.brand-mark{width:22px;height:22px;background:var(--red)}
.brand-name{font-family:"Ubuntu",sans-serif;font-weight:500;font-size:36px;color:var(--ink);letter-spacing:-.5px}
.social-top{right:38px;top:26px;display:flex;gap:3px}
.social-top span{width:16px;height:16px;border-radius:50%;background:#bdbdbd}
.main-nav{left:270px;top:69px;width:513px;height:33px;background:var(--nav);font-family:"Roboto",sans-serif;font-weight:300;font-size:10px;color:#e6e6e6;text-transform:uppercase}
.main-nav a{color:inherit;text-decoration:none;height:33px;display:flex;align-items:center;position:absolute;top:0;white-space:nowrap}
.main-nav .active{left:0;background:var(--red);width:63px;justify-content:center;color:var(--white)}
.nav-search{position:absolute;right:0;top:0;width:37px;height:33px;background:var(--red);display:flex;align-items:center;justify-content:center}
.header-rule{left:0;top:166px;width:816px;height:3px;background:var(--nav)}

/* hero */
.hero{left:0;top:169px;width:816px;height:293px;background:linear-gradient(180deg,#b9c1cb 0%,#d9dde3 45%,#eceef0 70%,#c9cdd2 100%)}
.hero-caption{left:0;top:462px;width:816px;height:48px;background:var(--nav)}
.hero-arrow{top:0;width:41px;height:48px;display:flex;align-items:center;justify-content:center;background:var(--red)}
.hero-arrow.prev{left:0}
.hero-arrow.next{left:42px;background:var(--red-deep)}
.hero-title{left:100px;right:0;top:0;height:48px;line-height:48px;text-align:center;font-family:"Roboto Condensed",sans-serif;font-weight:300;font-size:19.5px;color:var(--white)}

/* services */
.service{top:544px;width:246px;height:118px;background:var(--card-bg);border:1px solid #e4e4e4;text-align:center;box-shadow:0 4px 0 -1px #e2e2e2}
.service .head{display:flex;align-items:center;justify-content:center;gap:10px;margin-top:20px;font-family:"Ubuntu",sans-serif;font-weight:500;font-size:14px;color:var(--red)}
.service p{font-size:8.6px;line-height:16px;color:var(--grey-text);margin:10px 18px 0}
.service.featured{background:var(--red-deep);border-color:var(--red-deep);box-shadow:0 4px 0 -1px var(--red-bright)}
.service.featured .head,.service.featured p{color:var(--white)}

/* features */
.feature{top:696px;width:246px;height:156px;border:1px solid var(--line);border-radius:6px;background:var(--white);padding:16px 0 0 37px}
.feature h3{font-family:"Ubuntu",sans-serif;font-weight:500;font-size:13px;color:var(--blue);line-height:16px}
.feature p{font-family:"Ubuntu",sans-serif;font-size:8.6px;line-height:12.2px;color:#444;width:176px;margin-bottom:10px}

/* tweet bar */
.tweet-bar{left:0;top:885px;width:816px;height:34px;background:var(--tweet-bar)}
.tweet-tab{left:0;top:0}
.tweet-text{left:70px;top:0;line-height:34px;font-family:Arial,sans-serif;font-size:10.6px;color:var(--white)}

/* footer */
.footer{left:0;top:919px;width:816px;height:210px;background:var(--footer)}
.footer-brand{left:46px;top:30px;display:flex;align-items:center;gap:8px}
.footer-brand .brand-mark{width:18px;height:18px}
.footer-brand .brand-name{font-size:30px;color:var(--white)}
.footer-about{left:38px;top:118px;width:180px;font-size:8.6px;line-height:16.3px;color:var(--footer-text)}
.footer-col{top:46px}
.footer-col h4{font-family:"Open Sans",sans-serif;font-weight:700;font-size:11px;color:var(--white);display:flex;align-items:center;gap:14px;letter-spacing:.2px}
.footer-col h4::after{content:"";width:82px;border-top:1px dotted #8a8a8a}
.posts{left:311px;width:180px}
.posts ul{list-style:none;margin-top:17px}
.posts li{font-size:8.6px;color:var(--footer-text);height:24.5px;line-height:20px;border-bottom:1px solid #555}
.posts li:first-child{color:var(--red-bright)}
.posts li:last-child{border-bottom:0}
.contact{left:611px;width:180px}
.contact-map{left:611px;top:102px;width:180px;height:96px;background:radial-gradient(ellipse at center,rgba(255,255,255,.07),rgba(255,255,255,0) 70%)}
.contact p{font-size:8.6px;line-height:15px;color:var(--footer-text);position:relative}
.contact .addr{margin-top:16px}
.contact .phone{margin-top:15px}
.contact .mail{margin-top:15px}
.bottom-bar{left:0;top:1129px;width:816px;height:36px;background:var(--footer-deep);border-top:1px solid #2b2b2b}
.copyright{left:26px;top:0;line-height:36px;font-size:8.6px;color:#bbbbbb}
.social-bottom{right:30px;top:11px;display:flex;gap:16px}
.social-bottom span{width:12px;height:12px;border-radius:50%;background:#8c8c8c}
.social-bottom span:first-child{background:var(--red-bright)}
</style>
</head>
<body>
<div class="site">

  <header>
    <div class="abs brand"><span class="brand-mark"></span><span class="brand-name">Vexlink</span></div>
    <div class="abs social-top" aria-label="Social links"><span></span><span></span><span></span><span></span></div>
    <nav class="abs main-nav">
      <a class="active" href="#">Home</a>
      <a style="left:94px" href="#">About Us</a>
      <a style="left:173px" href="#">Product &amp; Services</a>
      <a style="left:321px" href="#">Satellite</a>
      <a style="left:401px" href="#">Contact</a>
      <span class="nav-search">
        <svg width="12" height="12" viewBox="0 0 12 12"><circle cx="5" cy="5" r="3.6" fill="none" stroke="#fff" stroke-width="1.6"/><line x1="7.6" y1="7.6" x2="10.8" y2="10.8" stroke="#fff" stroke-width="1.8" stroke-linecap="round"/></svg>
      </span>
    </nav>
    <div class="abs header-rule"></div>
  </header>

  <section>
    <div class="abs hero" role="img" aria-label="Photo of large satellite dish antennas against a cloudy sky"></div>
    <div class="abs hero-caption">
      <span class="abs hero-arrow prev"><svg width="22" height="22" viewBox="0 0 22 22"><circle cx="11" cy="11" r="10" fill="#fff"/><path d="M12.5 6.5 8 11l4.5 4.5" fill="none" stroke="#d8141c" stroke-width="2.4"/></svg></span>
      <span class="abs hero-arrow next"><svg width="22" height="22" viewBox="0 0 22 22"><circle cx="11" cy="11" r="10" fill="#fff"/><path d="M9.5 6.5 14 11l-4.5 4.5" fill="none" stroke="#c0090f" stroke-width="2.4"/></svg></span>
      <h1 class="abs hero-title">OUR OPERATIONS GLOBALLY ALSO OWN VARIOUS RETAIL OPERATIONS</h1>
    </div>
  </section>

  <section>
    <div class="abs service" style="left:25px">
      <div class="head">
        <svg width="34" height="22" viewBox="0 0 34 22" fill="#333"><circle cx="13" cy="6" r="5"/><path d="M2 22c0-7 5-10 11-10s11 3 11 10z"/><circle cx="23" cy="6" r="4.5"/><path d="M22 12c5 0 10 3 10 10h-6c0-4-1-7-4-10z"/></svg>
        Carrier Wholesale
      </div>
      <p>we provide international call termination</p>
    </div>
    <div class="abs service featured" style="left:285px">
      <div class="head">
        <svg width="26" height="24" viewBox="0 0 26 24" fill="none" stroke="#fff" stroke-width="2"><path d="M15 4H3v18h18V10"/><path d="M10 15l1-4 10-10 3 3-10 10z"/></svg>
        Call Center Termination
      </div>
      <p>we provide our network to call centers to be able to terminate their calls</p>
    </div>
    <div class="abs service" style="left:545px">
      <div class="head">
        <svg width="28" height="24" viewBox="0 0 28 24" fill="#333"><rect x="1" y="1" width="26" height="17" rx="1"/><rect x="4" y="4" width="20" height="11" fill="#f7f7f7"/><rect x="11" y="18" width="6" height="3"/><rect x="7" y="21" width="14" height="2"/></svg>
        Satellite
      </div>
      <p>we provide internet bandwidth via Satellite to customers from around the world</p>
    </div>
  </section>

  <section>
    <div class="abs feature" style="left:25px;padding-top:18px">
      <h3>Satellite Internet Access</h3>
      <p>Orbivane delivers worldwide broadband Internet access with SLA and full support of QoS, VPN, business quality VoIP and videoconferencing.</p>
      <h3>Global Coverage</h3>
      <p>Orbivane adds Calvory Halcyon-11N and Nordel Skies NX-12 to the fleet.</p>
    </div>
    <div class="abs feature" style="left:285px">
      <h3>Dedicated Bandwidth</h3>
      <p>Up to 155 Mbps per terminal, Orbivane dedicated bandwidth services empower world's premier remote networks.</p>
      <h3>Hybrid Services</h3>
      <p>Use satellite and terrestrial MPLS IP VPN circuits to build seamless IP-enabled networks.</p>
    </div>
    <div class="abs feature" style="left:545px;padding-left:40px">
      <h3>iLumen Evolution</h3>
      <p>Orbivane introduces new iLumen-enabled services employing DVB-S2 and ACM to Middle East and Africa.</p>
      <h3 style="margin-left:2px;margin-top:10px">Virtual Network Operator</h3>
      <p style="margin-left:2px">Orbivane offers the complete range of iLumen VNO solutions for satellite private networks worldwide.</p>
    </div>
  </section>

  <div class="abs tweet-bar">
    <svg class="abs tweet-tab" width="53" height="34" viewBox="0 0 53 34"><path d="M0 0h53l-8 34H0z" fill="#d8141c"/><circle cx="23" cy="17" r="6" fill="#fff"/></svg>
    <p class="abs tweet-text">General offers flexible Satellite Bandwidth Lease Services to accommodate our global satellite fleet's wide variety of C-band, Ka-band,</p>
  </div>

  <footer>
    <div class="abs footer">
      <div class="abs footer-brand"><span class="brand-mark"></span><span class="brand-name">Vexlink</span></div>
      <p class="abs footer-about">Lorem ipsum dolor sit amet, consectetuer adipiscing elit, sed diam nonummy nibh euismod tincidunt.</p>

      <div class="abs footer-col posts">
        <h4>LATEST POSTS</h4>
        <ul>
          <li>Claritas est etiam processus dynamicus</li>
          <li>Mirum est notare quam littera gothica</li>
          <li>Eodem modo typi lorem elit</li>
          <li>Nam liber tempor cum soluta</li>
        </ul>
      </div>

      <div class="abs contact-map" role="img" aria-label="Faint dotted world map"></div>
      <div class="abs footer-col contact">
        <h4>CONTACT US</h4>
        <p class="addr">Address: 1600 Harlow Street<br>Mountain View, Australia &nbsp;90210</p>
        <p class="phone">Phone: +381 22480 735</p>
        <p class="mail">E-mail: &nbsp;support@qorvanet.com</p>
      </div>
    </div>
    <div class="abs bottom-bar">
      <p class="abs copyright">2014 Copyright Vexlink i. All right reserved</p>
      <div class="abs social-bottom" aria-label="Social links"><span></span><span></span><span></span><span></span><span></span></div>
    </div>
  </footer>

</div>
</body>
</html>
```